Professional & Modern Website Design for Ridgeline Site Fittings

Our company, a leader in custom furniture and joinery solutions for mining camps, needs a website overhaul. Our current site is looking dated and underwhelming, and we’re seeking a design that truly reflects our professionalism and expertise.

To Whom Are We Speaking?
Our target audience includes asset managers, procurement professionals, and senior-level management from international mining companies. We need a website that speaks directly to these key decision-makers, showcasing our value and expertise.

What We’re Looking For:
Fresh & Modern Aesthetic: We want our website to captivate visitors with a contemporary and sleek design.
Professional Appeal: The new design should convey our commitment to high-quality craftsmanship and service.
Visual Impact: Showcase our custom furniture and joinery work with stunning visuals that highlight our capabilities.
Brochure Alignment: The design should mirror the style and aesthetics of our attached brochure to ensure brand consistency and visual harmony.
Logo & Branding: We want to keep our current logo and branding. The red color should be retained but used sparingly as an accent color to complement the overall design.
Brand Book Usage: Attached is our Brand Book for our Hotel and Accommodation Company. Please use only the correct colors and text from this Brand Book for our Ridgeline Site Fittings Brand to ensure consistency and coherence across our branding.
Structured Layout: We require a total of 8 pages, including:
Landing Page: Featuring a prominent contact button
About
Services: Interior Design, Manufacturing, Delivery & Installation
Products: Furniture Packages, Joinery, Upholstery, Beds & Bedding

Our Goals:
Elevate Our Brand: Create a site that mirrors our reputation and industry leadership.
Enhance User Experience: Ensure a seamless, engaging experience for visitors.
Showcase Our Work: Promote our projects and services with impact.

Must include:
Contact us button
Geographical Reach

Previous company website: www.ridgelinesitefittings.com.au (we wish to convert some of the content from this website to the new platform). Competitor websites that we like: www.tablorvex.com.au,

For functionality we would like it to be designed on Wix.

```html
<!DOCTYPE html>
<html lang="en">
<head>
<meta charset="utf-8">
<title>Ridgeline Site Fittings</title>
<link href="https://fonts.googleapis.com/css2?family=Lexend:wght@300;400;500;600&family=Poppins:wght@300;400;500;600&display=swap" rel="stylesheet">
<style>
:root{
  --red:#c8102e;
  --ink:#1c1c1c;
  --muted:#8a8a8a;
  --soft:#f6f6f6;
  --line:#e4e4e4;
  --btn:#8d8d8d;
  --dark:#2b2b2b;
  --gold:#c49a4a;
}
*{box-sizing:border-box;margin:0;padding:0}
html,body{width:1200px;height:4521px;overflow:hidden}
body{position:relative;background:#fff;font-family:"Poppins",sans-serif;color:var(--ink)}
.abs{position:absolute}
.brand{display:flex;align-items:center;gap:10px;font-family:"Lexend",sans-serif;font-weight:600;color:var(--ink)}
.brand-name{line-height:1.05;font-size:17px;letter-spacing:1px}
.brand-name small{display:block;font-size:10px;letter-spacing:1px;font-weight:600}

.hero{left:0;top:0;width:1156px;height:625px;
  background:
   radial-gradient(ellipse 14% 30% at 6% 52%,rgba(72,98,58,.55),transparent 100%),
   radial-gradient(ellipse 10% 26% at 90% 50%,rgba(72,98,58,.5),transparent 100%),
   radial-gradient(ellipse 22% 12% at 52% 70%,rgba(255,255,255,.9),transparent 100%),
   radial-gradient(ellipse 34% 10% at 55% 88%,rgba(104,138,150,.55),transparent 100%),
   linear-gradient(90deg,rgba(255,255,255,0) 0%,rgba(255,255,255,.55) 30%,rgba(255,255,255,.55) 70%,rgba(255,255,255,0) 100%),
   linear-gradient(180deg,#f4f2ed 0%,#ece8e0 45%,#e2dcd1 68%,#d8cebf 82%,#cbbfac 100%)}
.side-rail{left:1156px;top:0;width:44px;height:625px;background:var(--red)}
.side-rail .menu{position:absolute;left:13px;top:28px;width:18px}
.side-rail .menu i{display:block;height:2px;background:#fff;margin-bottom:5px}
.side-rail .dot{position:absolute;left:17px;width:10px;height:10px;border-radius:2px;background:#fff}
.side-rail .follow{position:absolute;left:16px;top:608px;transform:rotate(-90deg);transform-origin:left top;color:#fff;font-size:9px;white-space:nowrap}
.contact-link{left:1051px;top:29px;font-size:11px;font-weight:500;letter-spacing:.5px}

.intro-head{left:0;top:685px;width:1200px;text-align:center;font-family:"Lexend",sans-serif;font-size:36px;font-weight:300;line-height:50px}
.intro-head b{font-weight:600}
.band-grey{background:var(--soft)}
.welcome{left:260px;top:851px;width:680px;height:298px;background:#fff;box-shadow:0 6px 24px rgba(0,0,0,.06)}
.welcome .mark{position:absolute;left:44px;top:58px;width:130px;height:110px;background:var(--red)}
.welcome h2{position:absolute;left:216px;top:54px;font-family:"Lexend",sans-serif;font-weight:400;font-size:20px;line-height:23px}
.welcome h2 b{font-weight:600}
.welcome p{position:absolute;left:216px;top:110px;width:420px;font-size:10.5px;line-height:19px;color:var(--muted)}
.btn{display:inline-block;background:var(--btn);color:#fff;font-size:11px;padding:6px 18px}
.welcome .btn{position:absolute;left:216px;top:208px}

.section-label{font-family:"Lexend",sans-serif;font-size:17px;letter-spacing:1px;color:var(--muted);font-weight:500}
.service{width:279px;height:262px}
.service .photo{width:279px;height:205px}
.service .info{position:absolute;left:10px;top:190px;width:259px;height:80px;background:#fff;padding:16px 10px}
.service h3{font-size:14px;font-weight:600}
.service p{font-size:10.5px;line-height:14px;color:var(--muted);margin-top:4px;width:200px}
.arrow{position:absolute;width:22px;height:22px;border-radius:50%;background:#d7d7d7}
.arrow.on{background:var(--red)}
.arrow svg{position:absolute;left:6px;top:6px}

.products-photo{left:0;top:1632px;width:537px;height:566px;
  background:
   radial-gradient(ellipse 30% 38% at 52% 36%,rgba(48,42,36,.75),transparent 100%),
   radial-gradient(ellipse 40% 22% at 40% 80%,rgba(222,200,168,.8),transparent 100%),
   radial-gradient(ellipse 20% 60% at 10% 40%,rgba(120,95,70,.7),transparent 100%),
   linear-gradient(135deg,#d3c1a3 0%,#b39a78 40%,#7e6850 75%,#5c4c3d 100%)}
.product{left:619px;width:428px;height:95px;border-bottom:1px solid var(--line)}
.product svg.icon{position:absolute;left:12px;top:22px}
.product h4{position:absolute;left:88px;top:22px;font-size:14px;font-weight:500}
.product h4.hot{color:var(--red)}
.product p{position:absolute;left:88px;top:44px;width:300px;font-size:10.5px;line-height:14px;color:var(--muted)}
.product .arrow{left:403px;top:34px}

.goal h5{font-size:12px;font-weight:600}
.goal p{font-size:11px;line-height:17px;margin-top:8px}

.work .tag{position:absolute;background:#fff;padding:8px 16px;font-size:11.5px;font-weight:500;line-height:14px;box-shadow:0 4px 14px rgba(0,0,0,.06)}

.concept-photo{left:254px;top:3067px;width:790px;height:438px;
  background:
   radial-gradient(ellipse 22% 16% at 46% 56%,rgba(150,96,52,.9),transparent 100%),
   radial-gradient(ellipse 40% 28% at 55% 88%,rgba(24,44,96,.9),transparent 100%),
   radial-gradient(ellipse 18% 45% at 80% 45%,rgba(88,160,178,.75),transparent 100%),
   linear-gradient(180deg,#e6dfd6 0%,#b89a7a 30%,#6f5a48 60%,#25345a 100%)}
.panel{background:#fff}
.panel h2{font-family:"Lexend",sans-serif;font-weight:600;font-size:36px;line-height:37px}
.panel p{font-size:10.5px;line-height:19px;color:var(--muted)}

.geo h2{font-family:"Lexend",sans-serif;font-weight:600;font-size:36px;line-height:38px}
.geo p{font-size:10.5px;line-height:18px;color:var(--muted);margin-top:14px;width:280px}
.world{left:588px;top:3716px;width:368px;height:200px;
  background:
   radial-gradient(ellipse 16% 18% at 80% 76%,rgba(196,154,74,.85),transparent 100%),
   radial-gradient(ellipse 14% 16% at 66% 44%,rgba(196,154,74,.75),transparent 100%),
   radial-gradient(ellipse 20% 30% at 22% 40%,rgba(220,220,220,.9),transparent 100%),
   radial-gradient(ellipse 12% 28% at 30% 78%,rgba(225,225,225,.9),transparent 100%),
   radial-gradient(ellipse 26% 24% at 60% 30%,rgba(225,225,225,.9),transparent 100%),
   radial-gradient(ellipse 12% 22% at 50% 62%,rgba(225,225,225,.9),transparent 100%)}

.inquiry{left:293px;top:3961px;width:612px;height:310px;background:#fff;box-shadow:0 6px 24px rgba(0,0,0,.05)}
.inquiry h3{position:absolute;top:50px;width:100%;text-align:center;font-family:"Lexend",sans-serif;font-weight:400;font-size:17px;color:var(--muted)}
.field{position:absolute;border:1px solid var(--line);font-size:9.5px;color:#bbb;padding:7px 10px}
.inquiry .btn{position:absolute;left:266px;top:232px}

.footer{left:0;top:4160px;width:1200px;height:326px;background:var(--soft)}
.foot-brand .brand-name{font-size:28px;letter-spacing:2px}
.foot-brand .brand-name small{font-size:14px;letter-spacing:1px;font-weight:600}
.foot-text{font-size:11px;line-height:21px}
.foot-text .r{color:var(--red);font-weight:600}
.copy-bar{left:0;top:4486px;width:1200px;height:35px;background:var(--dark);color:#fff;font-size:10.5px}
</style>
</head>
<body>

<!-- Hero -->
<div class="abs hero" role="img" aria-label="Bright living room with white sofa, teal cushions, potted plants, round coffee table and blue rug"></div>
<div class="abs brand" style="left:30px;top:18px">
  <span class="brand-name">RIDGELINE<small>SITE FITTINGS</small></span>
</div>
<div class="abs contact-link">CONTACT US</div>
<div class="abs side-rail">
  <div class="menu"><i></i><i style="width:12px;margin-left:6px"></i><i></i></div>
  <span class="dot" style="top:475px"></span>
  <span class="dot" style="top:497px"></span>
  <span class="dot" style="top:519px"></span>
  <span class="dot" style="top:541px"></span>
  <span class="follow">Follow Us</span>
</div>

<!-- Intro -->
<div class="abs band-grey" style="left:0;top:1074px;width:1200px;height:558px"></div>
<h1 class="abs intro-head">Ridgeline Site Fittings Is Your Ultimate<br><b>Furniture Solutions Partner.</b></h1>
<section class="abs welcome">
  <div class="mark"></div>
  <h2>WELCOME To<br><b>Ridgeline Site Fittings</b></h2>
  <p>Welcome To Ridgeline Site Fittings, Your Trusted Partner For Custom Furniture Manufacturing. We Specialize In Delivering High-Quality Furniture Solutions Tailored To Your Specific Needs While Ensuring Stringent Quality Control And Efficient Project Management Throughout The Process.</p>
  <span class="btn">About Us</span>
</section>

<!-- Services -->
<div class="abs section-label" style="left:0;width:1200px;text-align:center;top:1220px">SERVICES</div>
<div class="abs service" style="left:156px;top:1268px">
  <div class="photo" role="img" aria-label="Furnished lounge interior with tall windows" style="background:radial-gradient(ellipse 30% 30% at 45% 30%,rgba(250,245,235,.9),transparent 100%),radial-gradient(ellipse 40% 20% at 60% 75%,rgba(200,180,150,.8),transparent 100%),linear-gradient(180deg,#cfc6b9 0%,#8e7f6d 55%,#5e5247 100%)"></div>
  <div class="info"><h3>Interior Design</h3><p>From concept development to space planning and material selection...</p><span class="arrow" style="left:222px;top:40px"><svg width="10" height="10" viewBox="0 0 10 10"><path d="M1 5h7M5 2l3 3-3 3" stroke="#fff" stroke-width="1.5" fill="none"/></svg></span></div>
</div>
<div class="abs service" style="left:460px;top:1268px">
  <div class="photo" role="img" aria-label="Craftsman assembling a timber model house" style="background:radial-gradient(ellipse 28% 30% at 50% 55%,rgba(232,204,160,.95),transparent 100%),radial-gradient(ellipse 30% 40% at 85% 20%,rgba(60,62,70,.7),transparent 100%),linear-gradient(160deg,#4f4038 0%,#8a6c50 50%,#b08860 100%)"></div>
  <div class="info"><h3>Manufacturing</h3><p>Our skilled craftsmen and advanced manufacturing capabilities...</p><span class="arrow" style="left:222px;top:40px"><svg width="10" height="10" viewBox="0 0 10 10"><path d="M1 5h7M5 2l3 3-3 3" stroke="#fff" stroke-width="1.5" fill="none"/></svg></span></div>
</div>
<div class="abs service" style="left:765px;top:1268px">
  <div class="photo" role="img" aria-label="Two delivery workers with an armchair" style="height:185px;background:radial-gradient(ellipse 40% 26% at 50% 78%,rgba(176,140,104,.95),transparent 100%),radial-gradient(ellipse 34% 30% at 50% 30%,rgba(60,70,88,.7),transparent 100%),linear-gradient(180deg,#c6ced6 0%,#9aa3ab 50%,#7a6b5c 100%)"></div>
  <div class="info" style="top:170px;box-shadow:0 4px 16px rgba(0,0,0,.07)"><h3>Delivery &amp; Installation</h3><p>Our dedicated project management team oversees all aspects...</p><span class="arrow on" style="left:222px;top:36px"><svg width="10" height="10" viewBox="0 0 10 10"><path d="M1 5h7M5 2l3 3-3 3" stroke="#fff" stroke-width="1.5" fill="none"/></svg></span></div>
</div>

<!-- Products -->
<div class="abs products-photo" role="img" aria-label="Carpenter working on timber in a workshop"></div>
<div class="abs section-label" style="left:619px;top:1702px">PRODUCTS</div>
<div class="abs" style="left:619px;top:1744px;width:428px;border-top:1px solid var(--line)"></div>
<div class="abs product" style="top:1744px">
  <svg class="icon" width="44" height="44" viewBox="0 0 44 44" fill="none" stroke="#333" stroke-width="1.6"><rect x="4" y="18" width="36" height="18"/><path d="M4 14h36M10 18v-8h8v8M26 18v-8h8v8M8 36v4M36 36v4M14 26h16"/></svg>
  <h4>Furniture Packages</h4><p>Our packages include robust and ergonomic bedroom furniture designed to maximize comfort...</p>
  <span class="arrow"><svg width="10" height="10" viewBox="0 0 10 10"><path d="M1 5h7M5 2l3 3-3 3" stroke="#fff" stroke-width="1.5" fill="none"/></svg></span>
</div>
<div class="abs product" style="top:1839px">
  <svg class="icon" width="44" height="44" viewBox="0 0 44 44" fill="none" stroke="#333" stroke-width="1.6"><path d="M6 16h32M8 16v22M36 16v22M14 16V8h16v8M14 26h16v12M14 32h16"/></svg>
  <h4>Joinery</h4><p>When it comes to joinery, we take great pride in our commitment to delivering exceptional quality...</p>
  <span class="arrow"><svg width="10" height="10" viewBox="0 0 10 10"><path d="M1 5h7M5 2l3 3-3 3" stroke="#fff" stroke-width="1.5" fill="none"/></svg></span>
</div>
<div class="abs product" style="top:1934px">
  <svg class="icon" width="44" height="44" viewBox="0 0 44 44" fill="none" stroke="#333" stroke-width="1.6"><path d="M10 38V12a8 8 0 0 1 16 0v26M6 38h30M30 38V24h6v14"/><rect x="14" y="20" width="8" height="12" fill="#c8102e" stroke="none"/></svg>
  <h4 class="hot">Upholstery</h4><p>When it comes to upholstery fabrics, we believe in using only the finest materials to ensure a...</p>
  <span class="arrow on"><svg width="10" height="10" viewBox="0 0 10 10"><path d="M1 5h7M5 2l3 3-3 3" stroke="#fff" stroke-width="1.5" fill="none"/></svg></span>
</div>
<div class="abs product" style="top:2029px">
  <svg class="icon" width="44" height="44" viewBox="0 0 44 44" fill="none" stroke="#333" stroke-width="1.6"><path d="M4 36V22h36v14M4 30h36M8 22v-6h28v6M22 4l4 4-4 4-4-4z"/></svg>
  <h4>Beds &amp; Bedding</h4><p>When it comes to beds, we are committed to providing you with the ultimate sleep experience...</p>
  <span class="arrow"><svg width="10" height="10" viewBox="0 0 10 10"><path d="M1 5h7M5 2l3 3-3 3" stroke="#fff" stroke-width="1.5" fill="none"/></svg></span>
</div>

<!-- Goals -->
<div class="abs band-grey" style="left:0;top:2198px;width:1200px;height:237px"></div>
<div class="abs section-label" style="left:200px;top:2308px">OUR GOALS</div>
<div class="abs goal" style="left:491px;top:2288px;width:220px"><h5>Elevate Our Brand:</h5><p>Create A Site That Mirrors Our Reputation And Industry Leadership.</p></div>
<div class="abs goal" style="left:786px;top:2291px;width:200px"><h5>Enhance User Experience:</h5><p>Ensure A Seamless, Engaging Experience For Visitors.</p></div>

<!-- Our Work -->
<div class="abs section-label" style="left:0;width:1200px;text-align:center;top:2509px">OUR WORK</div>
<div class="abs" role="img" aria-label="Hotel room interior" style="left:0;top:2575px;width:40px;height:237px;background:linear-gradient(160deg,#d6cec4,#8e857c 60%,#5a524b)"></div>
<div class="abs" role="img" aria-label="Hotel bedroom with teal bedding, television and city view" style="left:65px;top:2575px;width:340px;height:237px;background:radial-gradient(ellipse 30% 22% at 62% 78%,rgba(32,170,172,.9),transparent 100%),radial-gradient(ellipse 16% 18% at 30% 38%,rgba(30,30,32,.8),transparent 100%),radial-gradient(ellipse 40% 30% at 70% 28%,rgba(170,200,220,.8),transparent 100%),linear-gradient(180deg,#eef0f2 0%,#d7dadd 50%,#c9bfae 100%)"></div>
<div class="abs work"><span class="tag" style="left:82px;top:2780px;width:200px">Meridian Grand<br>Wellington, New Zealand</span></div>
<div class="abs" role="img" aria-label="Restaurant interior with wave timber ceiling and pendant lights" style="left:432px;top:2556px;width:447px;height:274px;background:radial-gradient(ellipse 60% 22% at 60% 18%,rgba(196,150,98,.95),transparent 100%),radial-gradient(ellipse 16% 30% at 12% 50%,rgba(60,140,170,.8),transparent 100%),radial-gradient(ellipse 50% 22% at 50% 88%,rgba(40,48,60,.85),transparent 100%),linear-gradient(180deg,#7a5436 0%,#a57a52 35%,#3f5a68 70%,#2b3442 100%)"></div>
<div class="abs work"><span class="tag" style="left:450px;top:2798px;width:330px;height:40px">Lakeshore Garden Hotel<br>Busselton, Western Australia</span>
  <span class="arrow on" style="left:737px;top:2808px"><svg width="10" height="10" viewBox="0 0 10 10"><path d="M1 5h7M5 2l3 3-3 3" stroke="#fff" stroke-width="1.5" fill="none"/></svg></span></div>
<div class="abs" role="img" aria-label="Lobby lounge with navy curtains and yellow armchairs" style="left:903px;top:2575px;width:297px;height:237px;background:radial-gradient(ellipse 40% 18% at 45% 72%,rgba(222,182,52,.9),transparent 100%),radial-gradient(ellipse 30% 14% at 50% 92%,rgba(150,150,158,.8),transparent 100%),linear-gradient(180deg,#1c2b52 0%,#2f4173 50%,#3d4a6e 75%,#8a8c96 100%)"></div>
<div class="abs work"><span class="tag" style="left:922px;top:2780px;width:200px">Harbourview<br>Auckland, New Zealand</span></div>
<div class="abs" style="left:425px;top:2900px;width:347px;height:1px;background:var(--line)"></div>
<div class="abs" style="left:593px;top:2895px;width:11px;height:11px;border-radius:50%;background:#333"></div>

<!-- Concept to completion -->
<div class="abs band-grey" style="left:0;top:2982px;width:1200px;height:676px"></div>
<div class="abs concept-photo" role="img" aria-label="Lounge with live-edge timber table and blue armchairs"></div>
<div class="abs panel" style="left:140px;top:3104px;width:350px;height:263px;padding:28px 16px 0 18px">
  <div style="font-size:10.5px;font-weight:500">We Have You Covered From</div>
  <h2 style="margin-top:8px">Concept To<br>Completion</h2>
  <p style="margin-top:14px">Whether You Require Interior Design Expertise, Assistance With Tender Submissions, Custom Joinery Solutions, Or Furniture And Room Prototypes, We Have The Expertise And Resources To Deliver Exceptional Results.</p>
</div>
<div class="abs panel" style="left:539px;top:3398px;width:461px;height:112px;padding:32px 0 0 33px"><h2>Durable, Functional<br>And Compliant</h2></div>
<div class="abs" style="left:572px;top:3522px;width:400px"><p style="font-size:10.5px;line-height:19px;color:var(--muted)">We Understand The Unique Demands Of Mining Operations And The Need For Durable, Functional, And Compliant Furniture Solutions. With Our Comprehensive Packages, We Aim To Create Comfortable And Efficient Living Spaces For Your Mining Workforce.</p></div>

<!-- Geographical Reach -->
<div class="abs geo" style="left:232px;top:3737px"><h2>Geographical<br>Reach</h2><p>With A Global Presence, Our Services Extend To Australia, New Zealand, South East Asia, And The United Arab Emirates.</p></div>
<div class="abs world" role="img" aria-label="World map highlighting Australia, New Zealand, South East Asia and the UAE"></div>

<!-- Footer band -->
<div class="abs footer"></div>

<!-- Inquiry -->
<section class="abs inquiry">
  <h3>Quick Inquiry</h3>
  <div class="field" style="left:50px;top:88px;width:250px;height:30px">Full Name</div>
  <div class="field" style="left:50px;top:130px;width:250px;height:30px">Email</div>
  <div class="field" style="left:50px;top:172px;width:250px;height:30px">Phone</div>
  <div class="field" style="left:312px;top:88px;width:250px;height:72px">How Can We Help?</div>
  <div class="abs" style="left:312px;top:178px;font-size:10px;color:var(--muted);display:flex;align-items:center;gap:8px"><span style="width:20px;height:20px;border-radius:50%;background:#e3e3e3;display:inline-block"></span>Attach File</div>
  <span class="btn">Submit</span>
</section>

<!-- Footer content -->
<div class="abs brand foot-brand" style="left:156px;top:4325px">
  <span class="brand-name">RIDGELINE<small>SITE FITTINGS</small></span>
</div>
<div class="abs foot-text" style="left:517px;top:4320px">
  If You Have Any Questions, Let Us Know.<br>
  <span class="r">P</span> <b>1300 555 014</b><br>
  <div style="height:8px"></div>
  <b>Marcus Hale MDIA</b><br>
  <span class="r">M</span> <b>+61 400 555 218</b><br>
  Marcus@Ridgelinesitefittings.Com.Au<br>
  Info@Ridgelinesitefittings.Com.Au
</div>
<div class="abs foot-text" style="left:909px;top:4320px">
  Part Of The
  <div style="display:flex;align-items:center;gap:8px;margin:8px 0 6px"><span style="width:32px;height:32px;border:2px solid var(--red);display:inline-block"></span><span style="font-family:'Lexend',sans-serif;font-size:14px;line-height:15px;letter-spacing:1px">HARBOURLINE<br>INTERIORS</span></div>
  Group Of Companies
</div>

<div class="abs copy-bar">
  <span class="abs" style="left:156px;top:11px">© 2024 Ridgeline Site Fittings. All Right Reserved</span>
  <span class="abs" style="left:998px;top:9px;width:17px;height:17px;border-radius:50%;background:var(--red)"></span>
  <span class="abs" style="left:1024px;top:9px;width:17px;height:17px;border-radius:50%;background:#fff"></span>
</div>

</body>
</html>
```